Uncoded front page web design for wedding and event planning company

Hi.

I am launching a wedding and event planning company called Silver Fern Gatherings and need a professional and appealing web design.

So, let me explain my company. I am based in Swindon in Wiltshire but the company will plan weddings and events in Oxfordshire, Wiltshire, Berkshire and London.

We will plan weddings, birthdays, conferences, product launches, fashion shows and conventions but the main focus of the website at this stage should be the weddings with all the other occasions being covered under a single 'events' heading.

My contact details for the website should be:
Marion Blake
marion@silverferngatherings.co.uk
01632 960457 / 07700 900583

I'd like the website to feel clean, bright and elegant and be set against a white or off-white background. My logo is purple and I'd therefore like some purple incorporated into the design although feel free to use a more muted purple as my one might be a little bright? I'm also considering whether it would look nice paired with a little of the colour gold - maybe as a font colour in places?? I'll leave you to figure that one out as your design eye will be better than mine but for your reference below is my purple colour and my suggested gold one....

My purple colour is Pantone 2592 C but feel free to use others
My suggested gold I'm looking at is Pantone 14-1041 TCX

I would like to incorporate a Circlebook feed in the front page if possible, if it looks right. I'd also like to include a variety of pictures as well so I've included a few in a Dropbox folder which is linked below. Please don't feel obliged to use them all by any means (there's loads!) but you've got a few there to play with. If you find any other royalty free images you'd rather use please go ahead but on the understanding I can have them afterwards!

My logo can be retrieved via this Dropbox link...
You'll notice there are 2 styles of placement. Please feel free to use either to fit in with your design...
https://www.filedrawer-example.com/sh/qk7pa2mwx9rn4lt/BBBKzq8ohPnvve4S03LoPjvb?dl=0

The wedding images I have are in this Dropbox folder...
https://www.filedrawer-example.com/sh/m8wd6rzp2lo4ye1/BBB4kqrXv8nWd7S05JmOgtlp?dl=0

Other than that, it's over to you.... I can't wait to receive your designs :-)

Ooh....finally just to say, as I receive designs in I think I'll notice aspects that I like and don't like and if I feel they'll be useful for other designers, I'll update my brief below. Thanks

BRIEF UPDATE:
Someone asked if I had a tag-line. Could you use "Creating exquisite occasions today for amazing memories tomorrow"

I realise I hadn't explained what I'd like included on my home page so here's some notes to consider....

A welcome to section for me to start narrative about us and our services which has a button that links to our 'about us' page and 'services' page for further information.

A section that nicely illustrates what services we offer whether that be with icons or pictures.

A section with some photos in that would link to our gallery

A section that shows some customer reviews and blog entries that would link to my reviews page and blog to read more.

And finally a contact us section with my details, social media links and site map.

***
I also need to draw attention to where in the UK my services cover. I was therefore thinking perhaps we could use a picture to demonstrate this where it highlights Wiltshire, Oxfordshire, Berkshire and London on a map thereby demonstrating our areas covered. I have found several English county maps when searching on Google but I'm not sure how to highlight the areas I cover (or dull out the areas I don't) so if you have any ideas on this, I'd really like it incorporated. Thanks. (by the way, for those of you not familiar with English counties, the ones I cover are often abbreviated to Wilts, Oxon, Berks, London, so if you find a suitable map with those names on rather than the full names, you'll know what they are!)

I've found an image of the county map which might work well. I was wondering whether we might somehow grey out the counties I don't cover and just keep the ones I do as mentioned above and then crop it into perhaps a shadowed circle? I've attached a screenshot to the brief.
Updates

I've decided on the tag-line "Creating exquisite occasions today for amazing memories tomorrow" so if that could be included somewhere that would be great. I also need to draw attention to where in the UK my services cover. I was therefore thinking perhaps we could use a picture to demonstrate this where it highlights Wiltshire, Oxfordshire, Berkshire and London on a map thereby demonstrating our areas covered. I have found several English county maps when searching on Google but I'm not sure how to highlight the areas I cover (or dull out the areas I don't) so if you have any ideas on this, I'd really like it incorporated. Thanks. Added Wednesday, June 24, 2015

Target Market(s)

Predominately women aged 25-55

Industry/Entity Type

Wedding Planner

Number of Pages Required

1 page

Font styles to use
Sans Serif
Script

Requirements
Nice to have
• I'd like to see how the colour theme of purple and perhaps a little gold (maybe as a font colour) look against a white background. I've mentioned the Pantone colours in the brief above.
• I've attached a screenshot of a webpage with gold writing in and fonts that I like. Perhaps it could give you inspiration?
Should not have
• I really don't like the font QUILLORA so please done use that.

```html
<!DOCTYPE html>
<html lang="en">
<head>
<meta charset="utf-8">
<title>Silver Fern Gatherings – Weddings &amp; Events</title>
<link href="https://fonts.googleapis.com/css2?family=Raleway:wght@400;500;600;700&family=Open+Sans:wght@400;600&display=swap" rel="stylesheet">
<style>
:root{
  --purple:#8a2fb3;
  --purple-dark:#6f2093;
  --gold:#e2a84c;
  --gold-light:#f0cf8c;
  --text:#555;
  --muted:#888;
  --line:#e6e1d8;
  --bg:#ffffff;
  --grey:#f1f0ee;
  --social-blue:#3d6a98;
}
*{box-sizing:border-box;margin:0;padding:0}
html,body{width:1200px;height:4337px;overflow:hidden;background:var(--bg)}
body{position:relative;font-family:"Open Sans",Arial,sans-serif;color:var(--text);font-size:15px}
.section{position:absolute;left:0;width:1200px}
.heading-font{font-family:"Raleway",Arial,sans-serif}

/* header */
.site-header{top:0;height:126px;border-bottom:3px solid var(--gold-light)}
.brand{position:absolute;left:72px;top:34px;display:flex;align-items:center;gap:14px}
.brand-dot{width:50px;height:50px;border-radius:50%;background:var(--purple)}
.brand-name{font-family:"Raleway",sans-serif;font-weight:600;font-size:30px;color:var(--purple)}
.main-nav{position:absolute;right:72px;top:52px;display:flex;gap:34px;font-family:"Raleway",sans-serif;font-size:15px;letter-spacing:1px}
.main-nav a{color:#666;text-decoration:none}
.main-nav a.active{color:var(--gold)}

/* hero */
.hero{top:129px;height:576px;background:linear-gradient(90deg,#fbfaf7 0%,#f6f2ec 40%,#e8ddd2 60%,#d9c7b8 80%,#eee6dc 100%)}
.hero-photo{position:absolute;right:0;top:0;width:620px;height:576px;background:radial-gradient(ellipse at 55% 45%,#e9d8c9,#cdb4a1 55%,#efe8e0 100%)}
.tagline{position:absolute;left:72px;top:130px;font-family:"Raleway",sans-serif;font-size:36px;line-height:50px;color:var(--gold);font-weight:500}
.tagline strong{color:var(--purple);font-weight:600}
.slider-dots{position:absolute;left:72px;top:540px;display:flex;gap:8px}
.slider-dots span{width:12px;height:12px;border-radius:50%;background:#ccc}
.slider-dots span:first-child{background:#999}

/* welcome */
.welcome{top:752px;left:72px;width:1056px;height:310px;border:2px solid var(--gold-light);outline:1px solid var(--gold-light);outline-offset:-10px;text-align:center;padding:40px 90px 0}
.welcome h1{font-family:"Raleway",sans-serif;font-weight:500;font-size:30px;color:var(--purple)}
.welcome .lead{margin-top:10px;font-size:17px;color:#555}
.welcome p.body{margin-top:30px;font-size:14px;line-height:26px;color:var(--muted)}

/* services */
.services{top:1084px;height:542px;background:linear-gradient(180deg,#d7cbb8 0%,#eeeae3 35%,#f6f5f2 65%,#e4ddd2 100%)}
.service{position:absolute;width:170px;height:170px;border-radius:50%;background:#fff;border:4px double #ccc;display:flex;flex-direction:column;align-items:center;justify-content:center;gap:8px}
.service .icon{width:64px;height:64px;border-radius:50%;background:var(--purple)}
.service .label{font-family:"Raleway",sans-serif;font-size:15px;color:#444;text-align:center;line-height:17px}

/* section titles */
.section-title{position:absolute;left:0;width:1200px;display:flex;align-items:center;justify-content:center;gap:24px;font-family:"Raleway",sans-serif;font-size:28px;color:var(--gold)}
.section-title::before,.section-title::after{content:"";width:150px;height:1px;background:var(--gold-light)}

/* blog */
.blog-card{position:absolute;top:1753px;width:326px;height:452px;border:1px solid var(--line);box-shadow:0 0 6px rgba(0,0,0,.08);padding:22px}
.blog-card .thumb{height:200px}
.blog-card h3{margin-top:18px;font-size:15px;font-weight:600;color:#333}
.blog-card p{margin-top:12px;font-size:13px;line-height:21px;color:var(--muted)}
.blog-card .meta{margin-top:16px;font-size:11px;color:#999}
.blog-card .meta b{color:var(--purple);font-weight:400}

.strap{position:absolute;top:2270px;width:1200px;text-align:center;font-family:"Raleway",sans-serif;font-size:26px;color:var(--gold)}
.strap-sub{position:absolute;top:2320px;width:1200px;text-align:center;font-size:15px;color:#666}
.gallery-strip{top:2385px;height:398px;display:flex}
.gallery-strip div{flex:1}

/* social */
.social-col{position:absolute;top:2845px}
.social-head{display:flex;align-items:center;gap:14px}
.social-badge{width:60px;height:60px;border-radius:50%;background:var(--social-blue)}
.social-head small{display:block;font-size:12px;color:#777;letter-spacing:1px}
.social-head span{font-family:"Raleway",sans-serif;font-size:30px;color:var(--social-blue)}
.insta-title{margin-top:22px;font-weight:600;color:var(--social-blue);font-size:15px}
.insta-text{margin-top:10px;font-size:13px;line-height:21px;color:#666}
.insta-photos{margin-top:18px;display:flex;gap:14px}
.insta-photos div{width:150px;height:112px}
.follow-btn{margin-top:22px;display:inline-block;background:var(--social-blue);color:#fff;font-size:14px;padding:12px 20px}
.feed{margin-top:20px;width:440px;height:362px;border:1px solid #ddd;padding:16px}
.feed-top{display:flex;gap:12px;align-items:center}
.feed-top .avatar{width:44px;height:44px;background:#d8c6e4}
.feed-top b{font-size:12px;color:var(--social-blue)}
.feed-top .like{display:inline-block;margin-top:4px;background:#4e69a2;color:#fff;font-size:10px;padding:2px 6px}
.feed-count{margin-top:14px;font-size:12px;color:#666}
.feed-grid{margin-top:10px;display:grid;grid-template-columns:repeat(6,56px);gap:8px}
.feed-grid span{height:56px;background:#cbb8a8}
.feed-foot{margin-top:14px;font-size:11px;color:#999}
.divider-v{position:absolute;left:600px;top:2830px;width:1px;height:470px;background:var(--line)}
.top-rule{position:absolute;top:2819px;left:0;width:1200px;height:1px;background:var(--line)}

/* testimonials */
.testimonial{position:absolute;top:3470px;left:150px;width:900px;text-align:center;font-size:14px;line-height:26px;color:#666}
.quote-mark{position:absolute;top:3425px;left:586px;width:30px;height:26px;border:2px solid var(--purple);border-radius:4px}
.client-name{position:absolute;top:3648px;width:1200px;text-align:center;color:var(--purple);font-weight:600;letter-spacing:1px}
.client-role{position:absolute;top:3672px;width:1200px;text-align:center;font-size:11px;color:#999}
.client-avatar{position:absolute;top:3698px;left:568px;width:64px;height:64px;border:2px solid var(--line);background:#d9b9a1}

/* newsletter */
.newsletter{top:3813px;height:101px;background:var(--purple);color:#fff}
.newsletter .nl-icon{position:absolute;left:130px;top:32px;width:36px;height:30px;border:2px solid #fff;border-radius:3px}
.newsletter h4{position:absolute;left:180px;top:26px;font-size:19px;font-weight:600}
.newsletter p{position:absolute;left:180px;top:56px;font-size:13px}
.nl-input{position:absolute;left:630px;top:34px;width:300px;height:34px;background:#fff;color:#aaa;font-size:12px;padding:9px 12px}
.nl-btn{position:absolute;left:936px;top:34px;width:120px;height:34px;background:var(--purple-dark);font-size:13px;text-align:center;line-height:34px;letter-spacing:1px}

/* contact */
.contact{top:3914px;height:351px;background:var(--grey);text-align:center}
.contact h2{margin-top:34px;font-family:"Raleway",sans-serif;font-weight:500;font-size:28px;color:var(--gold)}
.contact .sub{margin-top:6px;font-size:14px;color:#666}
.contact-cols{position:absolute;top:125px;left:72px;width:1056px;display:flex;justify-content:space-between}
.contact-col{width:240px;font-size:12px;line-height:18px;color:#666}
.contact-col .ic{margin:0 auto 12px;width:54px;height:54px;border-radius:50%;background:var(--purple);display:flex;align-items:center;justify-content:center}
.contact-col b{display:block;font-size:14px;color:#333;font-weight:600;margin-bottom:4px}
.contact .notice{position:absolute;top:290px;width:1200px;font-size:12px;line-height:18px;color:#888}

.site-footer{top:4265px;height:72px;border-top:1px solid var(--line)}
.site-footer .copy{position:absolute;left:72px;top:28px;font-size:12px;color:#888}
.footer-social{position:absolute;right:72px;top:20px;display:flex;gap:8px}
.footer-social span{width:32px;height:32px;border-radius:50%;background:#777}
.arrow{position:absolute;top:3545px}
</style>
</head>
<body>

<header class="section site-header">
  <div class="brand"><span class="brand-dot"></span><span class="brand-name">Silver Fern Gatherings</span></div>
  <nav class="main-nav">
    <a class="active" href="#">HOME</a><a href="#">ABOUT</a><a href="#">SERVICES</a><a href="#">GALLERY</a><a href="#">BLOG</a><a href="#">CONTACT ME</a>
  </nav>
</header>

<section class="section hero">
  <div class="hero-photo" role="img" aria-label="Bride in a lace gown holding a bouquet of pastel flowers"></div>
  <div class="tagline">Creating exquisite occasions <strong>today</strong><br>for amazing memories <strong>tomorrow</strong></div>
  <div class="slider-dots"><span></span><span></span><span></span><span></span><span></span></div>
</section>

<section class="section welcome">
  <h1>Welcome to Silver Fern Gatherings</h1>
  <p class="lead">The company will plan weddings and events in Oxfordshire, Wiltshire, Berkshire and London.</p>
  <p class="body">We bring calm planning, warm care and fine detail to every celebration. From the first idea to the final dance, our team shapes each moment around you, so your day feels effortless, personal and beautifully remembered for years to come.</p>
</section>

<section class="section services" role="img" aria-label="Reception hall with white dressed tables and chairs">
  <div class="service" style="left:258px;top:174px"><span class="icon"></span><span class="label">Flowers</span></div>
  <div class="service" style="left:775px;top:174px"><span class="icon"></span><span class="label">Ceremony</span></div>
  <div class="service" style="left:95px;top:295px"><span class="icon"></span><span class="label">Wedding<br>Cakes</span></div>
  <div class="service" style="left:367px;top:295px"><span class="icon"></span><span class="label">Wedding<br>Cars</span></div>
  <div class="service" style="left:649px;top:295px"><span class="icon"></span><span class="label">Wedding<br>Venues</span></div>
  <div class="service" style="left:920px;top:295px"><span class="icon"></span><span class="label">Photography</span></div>
</section>

<h2 class="section-title" style="top:1670px">From The Blog</h2>

<article class="blog-card" style="left:72px">
  <div class="thumb" role="img" aria-label="Bride smiling in a veil" style="background:linear-gradient(135deg,#d7b9a6,#8f6f63)"></div>
  <h3>Lorem Ipsum dolor amet sit</h3>
  <p>Fresh ideas for flowers, venues and styling to help you plan a day that feels truly yours.</p>
  <div class="meta">20 Mar 2015 | by <b>Tom Ashby</b> | 0 Comments</div>
</article>
<article class="blog-card" style="left:437px">
  <div class="thumb" role="img" aria-label="Plated wedding breakfast being served" style="background:linear-gradient(135deg,#e9e2d8,#a98a6d)"></div>
  <h3>Lorem Ipsum dolor amet sit</h3>
  <p>Simple menu tips for a wedding breakfast your guests will talk about long after the toasts.</p>
  <div class="meta">20 Mar 2015 | by <b>Tom Ashby</b> | 0 Comments</div>
</article>
<article class="blog-card" style="left:802px">
  <div class="thumb" role="img" aria-label="Couple celebrating under confetti" style="background:linear-gradient(135deg,#c06a8a,#5a2f4a)"></div>
  <h3>Lorem Ipsum dolor amet sit</h3>
  <p>How to choose music, lighting and little touches that turn an evening party into magic.</p>
  <div class="meta">20 Mar 2015 | by <b>Tom Ashby</b> | 0 Comments</div>
</article>

<div class="strap">Making the Most Important Day in Your Life a Happy One</div>
<div class="strap-sub">Find Wedding planner and consultant for your special and unique wedding</div>

<section class="section gallery-strip">
  <div role="img" aria-label="Bride's lace gown being laced up at the back" style="background:linear-gradient(135deg,#efe6dc,#c9b3a2)"></div>
  <div role="img" aria-label="Couple dancing in a candlelit hall" style="background:linear-gradient(135deg,#6b5446,#2f241e)"></div>
  <div role="img" aria-label="Hands with rings and a white rose bouquet" style="background:linear-gradient(135deg,#e0d3c8,#9c8477)"></div>
</section>

<div class="top-rule"></div>
<div class="divider-v"></div>

<div class="social-col" style="left:72px;width:480px">
  <div class="social-head"><span class="social-badge"></span><div><small>FOLLOW US ON</small><span>PICTUREGRAM</span></div></div>
  <div class="insta-title">@ Wedding Events</div>
  <p class="insta-text">See our latest weddings, table settings and floral details as they happen. Follow along for fresh ideas and behind-the-scenes moments from every event we plan.</p>
  <div class="insta-photos">
    <div role="img" aria-label="Wedding couple portrait" style="background:linear-gradient(135deg,#9fb2c2,#5d6f80)"></div>
    <div role="img" aria-label="Purple table flowers" style="background:linear-gradient(135deg,#b79ad0,#6d4c8a)"></div>
    <div role="img" aria-label="White vintage wedding car" style="background:linear-gradient(135deg,#ecebe6,#a9a59a)"></div>
  </div>
  <div class="follow-btn">Follow Us On Picturegram</div>
</div>

<div class="social-col" style="left:640px;width:488px">
  <div class="social-head"><span class="social-badge"></span><div><small>FOLLOW US ON</small><span>CIRCLEBOOK</span></div></div>
  <div class="feed">
    <div class="feed-top"><span class="avatar"></span><div><b>SILVER FERN GATHERINGS</b><br><span class="like">Like</span></div></div>
    <div class="feed-count">526 people like <b style="color:var(--social-blue)">Silver Fern Gatherings</b></div>
    <div class="feed-grid" role="img" aria-label="Grid of follower profile pictures">
      <span></span><span></span><span></span><span></span><span></span><span></span>
      <span></span><span></span><span></span><span></span><span></span><span></span>
      <span></span><span></span><span></span><span></span><span></span><span></span>
    </div>
    <div class="feed-foot">Social plugin</div>
  </div>
</div>

<h2 class="section-title" style="top:3362px">Client Success Stories</h2>
<div class="quote-mark"></div>
<svg class="arrow" style="left:90px" width="16" height="24" viewBox="0 0 16 24"><path d="M13 2 3 12l10 10" fill="none" stroke="#777" stroke-width="2.5"/></svg>
<svg class="arrow" style="left:1094px" width="16" height="24" viewBox="0 0 16 24"><path d="M3 2l10 10L3 22" fill="none" stroke="#777" stroke-width="2.5"/></svg>
<p class="testimonial">“ In publishing and graphic design, lorem ipsum is a filler text commonly used to demonstrate the graphic elements of a document or visual presentation. Replacing meaningful content with placeholder text allows viewers to focus on graphic aspects such as font, typography, and page layout without being distracted by the content. It also reduces the need for the designer to come up with meaningful text, as they can instead use quickly-generated lorem ipsum. ”</p>
<div class="client-name">ROSALIND</div>
<div class="client-role">Lorem ipsum dolor sit amet</div>
<div class="client-avatar" role="img" aria-label="Client portrait"></div>

<section class="section newsletter">
  <span class="nl-icon"></span>
  <h4>Subscribe our newsletter!</h4>
  <p>Enter your email address and receive latest news &amp; Updates</p>
  <div class="nl-input">Email Address</div>
  <div class="nl-btn">SUBSCRIBE</div>
</section>

<section class="section contact">
  <h2>Contact Us For More Information!</h2>
  <p class="sub">Send us an email and we'll get back to you right away!</p>
  <div class="contact-cols">
    <div class="contact-col"><div class="ic"><svg width="22" height="28" viewBox="0 0 22 28"><path d="M11 1a9 9 0 0 1 9 9c0 7-9 17-9 17S2 17 2 10a9 9 0 0 1 9-9z" fill="#fff"/><circle cx="11" cy="10" r="3.5" fill="#8a2fb3"/></svg></div><b>Silver Fern Gatherings</b>12 Meadow Lane, Old Town,<br>Swindon SN1 4AB</div>
    <div class="contact-col"><div class="ic"><svg width="24" height="24" viewBox="0 0 24 24"><path d="M6 2h4l2 5-3 2a12 12 0 0 0 6 6l2-3 5 2v4a2 2 0 0 1-2 2C10 20 4 14 4 4a2 2 0 0 1 2-2z" fill="#fff"/></svg></div><b>Telephone</b>01632 960457<br>07700 900583</div>
    <div class="contact-col"><div class="ic"><svg width="26" height="22" viewBox="0 0 26 22"><rect x="3" y="6" width="20" height="13" rx="2" fill="#fff"/><rect x="7" y="1" width="12" height="6" fill="#fff"/></svg></div><b>Telefax</b>01632 960457</div>
    <div class="contact-col"><div class="ic"><svg width="26" height="20" viewBox="0 0 26 20"><rect x="1" y="2" width="24" height="16" rx="2" fill="#fff"/><path d="M2 3l11 9 11-9" fill="none" stroke="#8a2fb3" stroke-width="2"/></svg></div><b>Email Address</b>marion@silverferngatherings.co.uk</div>
  </div>
  <p class="notice">All incoming emails will be answered within 24 hours (and normally within a few hours).<br>Please check your spam folder in case you haven't received an answer from us within 24 hours.</p>
</section>

<footer class="section site-footer">
  <div class="copy">Copyright ©2015 Silver Fern Gatherings. All rights reserved. | Terms of service | Privacy Policy</div>
  <div class="footer-social"><span></span><span></span><span></span><span></span></div>
</footer>

</body>
</html>
```